Finch Haulage Ltd

We need an A5 size (UK size) flyer to advertise our new business which is called Finch Haulage.
Domestic and Commercial Waste Clearance Services.
Please have the question in bold "Do you have a pile of junk you need to dispose of?"
We collect all kinds of junk or rubbish from homes and businesses across Kent, Sussex and South London.
No fuss, no mess!
A low cost, hassle free alternative to skip hire.
Licensed by the Landcare Board and fully insured (this can be in small print at the bottom).
Please put the Recycle symbol somewhere.
Our tagline on our vehicle is "We Clear More, For Less!"
We'd like the flyer to be bold and eye-catching (to catch the eye of the homeowner or business owner while it's sitting on their doormat).
We need our telephone, website and email to be prominent. Maybe saying "Call today for a free quote"
Tel. 01734 586019
Email: info@finchhaulage.example.co.uk
www.finchhaulage.example.co.uk
Target Market(s)
Our market will be homes and small businesses around Kent, Sussex and South London.

```html
<!DOCTYPE html>
<html lang="en">
<head>
<meta charset="utf-8">
<title>Finch Haulage – Waste Clearance Flyer</title>
<link rel="stylesheet" href="https://fonts.googleapis.com/css2?family=Jost:wght@400;500;600;700&family=Open+Sans:wght@700&display=swap">
<style>
  :root {
    --backdrop: #e6e6e6;
    --paper: #ffffff;
    --brand-green: #2fa956;
    --cab-green: #3a9e45;
    --cargo-green: #2e7d32;
    --text-green: #2fa84f;
    --ink-grey: #5a5a5a;
    --soft-grey: #6e6e6e;
  }
  html, body {
    margin: 0;
    padding: 0;
    width: 1200px;
    height: 1000px;
    overflow: hidden;
    background: var(--backdrop);
    font-family: "Jost", "Futura", sans-serif;
  }
  .flyer {
    position: absolute;
    left: 318px;
    top: 99px;
    width: 562px;
    height: 801px;
    background: var(--paper);
    box-shadow: 3px 3px 6px rgba(0,0,0,0.18);
    overflow: hidden;
  }
  .hero-band {
    position: absolute;
    left: 0;
    top: 0;
    width: 562px;
    height: 397px;
    background: var(--brand-green);
  }
  .hero-band-tail {
    position: absolute;
    left: 0;
    top: 397px;
    width: 292px;
    height: 66px;
    background: var(--brand-green);
  }
  .headline {
    position: absolute;
    left: 46px;
    top: 42px;
    margin: 0;
    color: var(--paper);
    font-weight: 700;
    font-size: 65px;
    line-height: 66.5px;
    letter-spacing: 2px;
    text-transform: uppercase;
  }
  .truck {
    position: absolute;
    left: 290px;
    top: 397px;
    width: 218px;
    height: 82px;
    background: var(--cab-green);
    border-radius: 3px;
  }
  .truck-tagline {
    position: absolute;
    left: 22px;
    top: 10px;
    margin: 0;
    color: var(--paper);
    font-family: "Open Sans", sans-serif;
    font-weight: 700;
    font-size: 13px;
    line-height: 20px;
    letter-spacing: 0.6px;
    text-transform: uppercase;
  }
  .service-copy {
    position: absolute;
    left: 45px;
    top: 502px;
    width: 240px;
    color: var(--text-green);
    font-size: 12.5px;
    font-weight: 500;
    line-height: 20.5px;
    letter-spacing: 2px;
    text-transform: uppercase;
  }
  .service-copy p { margin: 0 0 20px; }
  .brand-name {
    position: absolute;
    left: 296px;
    top: 520px;
    margin: 0;
    color: var(--ink-grey);
    font-size: 22px;
    font-weight: 600;
    letter-spacing: 1.5px;
    text-transform: uppercase;
  }
  .call-to-action {
    position: absolute;
    left: 297px;
    top: 586px;
    margin: 0;
    color: var(--soft-grey);
    font-size: 12.5px;
    line-height: 20.5px;
    letter-spacing: 2px;
    text-transform: uppercase;
  }
  .contact-list {
    position: absolute;
    left: 297px;
    top: 646px;
    margin: 0;
    padding: 0;
    list-style: none;
    color: var(--soft-grey);
    font-size: 11px;
    line-height: 20.5px;
    letter-spacing: 1.2px;
    text-transform: uppercase;
  }
  .licence-note {
    position: absolute;
    left: 19px;
    top: 762px;
    margin: 0;
    color: var(--soft-grey);
    font-size: 9.5px;
    letter-spacing: 2.4px;
    text-transform: uppercase;
  }
  .recycle-icon {
    position: absolute;
    left: 511px;
    top: 756px;
    width: 34px;
    height: 32px;
  }
</style>
</head>
<body>
  <main class="flyer">
    <div class="hero-band"></div>
    <div class="hero-band-tail"></div>
    <h1 class="headline">Do you<br>have a pile<br>of junk<br>you need to<br>dispose of?</h1>

    <div class="truck" role="img" aria-label="Illustration of a green haulage truck carrying the company tagline">
      <p class="truck-tagline">We clear more,<br>for less!</p>
    </div>

    <section class="service-copy">
      <p>We collect all kinds of junk or rubbish from homes and businesses across Kent, Sussex and South London.</p>
      <p>No fuss, no mess!</p>
      <p>A low cost, hassle free alternative to skip hire.</p>
    </section>

    <p class="brand-name">Finch Haulage</p>
    <p class="call-to-action">Call today<br>for a free quote</p>
    <ul class="contact-list">
      <li>Tel. 01734 586019</li>
      <li>info@finchhaulage.example.co.uk</li>
      <li>www.finchhaulage.example.co.uk</li>
    </ul>

    <p class="licence-note">Licensed by the Landcare Board and fully insured</p>

    <svg class="recycle-icon" viewBox="0 0 34 32" aria-label="Recycle symbol" role="img">
      <g fill="none" stroke="var(--brand-green)" stroke-width="3.5" stroke-linejoin="round">
        <path d="M12 6 L17 2 L22 10"/>
        <path d="M27 14 L31 22 L25 28"/>
        <path d="M17 28 L4 28 L8 20"/>
      </g>
      <g fill="var(--brand-green)">
        <polygon points="19,12 26,10 24,4"/>
        <polygon points="20,28 25,23 25,32"/>
        <polygon points="4,16 12,18 6,24"/>
      </g>
    </svg>
  </main>
</body>
</html>
```